Migration Lawyers

Company: Dunstan & Co Lawyers & Migration Agents

Name: Graham Dunstan BEc, LLB
Address: Level 18, 72 Hollis Street
Sydney, NSW, Australia 2000

Ph: +61 2 9384 5207
M: 0428316540
E: graham@permitpath-example.org.au
W: www.permitpath-example.org.au

Target Market(s)

Migration Clients

Industry/Entity Type

It Company

Font styles to use
Script

Requirements
Must have
• Logo
Should not have
• Please scale the format to the printing size attached

```html
<!DOCTYPE html>
<html lang="en">
<head>
<meta charset="utf-8">
<title>Dunstan &amp; Co — Business Card</title>
<link rel="stylesheet" href="https://fonts.googleapis.com/css2?family=Tinos:wght@400;700&family=Open+Sans:wght@400&display=swap">
<style>
  :root {
    --backdrop: #e9e6e1;
    --paper: #ffffff;
    --ink: #111111;
    --ink-soft: #3a3a3a;
    --grey: #555555;
    --rule: #9a9a9a;
    --accent: #e0201b;
    --night: #000000;
    --on-night: #f2f2f2;
  }
  * { margin: 0; padding: 0; box-sizing: border-box; }
  html, body { width: 1200px; height: 1136px; overflow: hidden; }
  body { background: var(--backdrop); position: relative; }

  .card {
    position: absolute;
    width: 885px;
    height: 506px;
    overflow: hidden;
    box-shadow: 0 2px 6px rgba(0,0,0,.18);
  }
  .card--front { left: 288px; top: 43px; background: var(--paper); }
  .card--back { left: 45px; top: 587px; background: var(--night); }

  /* brand */
  .brand-mark {
    position: absolute; left: 196px; top: 34px;
    width: 136px; height: 136px; border-radius: 50%;
    border: 3px solid var(--ink);
  }
  .brand-name {
    position: absolute; left: 366px; top: 38px;
    font-family: "Tinos", serif; font-weight: 700; color: var(--ink);
  }
  .brand-name__main { display: block; font-size: 58px; line-height: 64px; }
  .brand-name__sub { display: block; font-size: 21px; line-height: 28px; margin-top: 2px; }

  /* person */
  .person {
    position: absolute; right: 482px; top: 254px; text-align: right;
  }
  .person__name { font-family: "Tinos", serif; font-weight: 700; font-size: 26px; color: var(--ink); line-height: 36px; }
  .person__degree { font-family: "Tinos", serif; font-size: 24px; color: var(--grey); line-height: 34px; }
  .person__address {
    font-family: "Open Sans", sans-serif; font-size: 18px; color: var(--ink-soft);
    line-height: 33px; margin-top: 6px; font-style: normal;
  }
  .divider {
    position: absolute; left: 418px; top: 250px; width: 2px; height: 150px; background: var(--rule);
  }

  /* contacts */
  .contacts { position: absolute; left: 434px; top: 260px; list-style: none; }
  .contacts li {
    display: flex; align-items: center; height: 37px;
    font-family: "Open Sans", sans-serif; font-size: 19px; color: var(--ink-soft);
  }
  .contacts svg { width: 20px; height: 20px; margin-right: 10px; flex: none; }

  .wave { position: absolute; left: 0; top: 0; }

  /* back */
  .back-mark {
    position: absolute; left: 285px; top: 35px; width: 326px; height: 326px;
    border-radius: 50%; border: 3px solid var(--on-night);
    display: flex; align-items: center; justify-content: center;
  }
  .back-mark__name {
    font-family: "Tinos", serif; font-weight: 700; font-size: 44px; color: var(--on-night);
  }
  .back-url {
    position: absolute; left: 234px; top: 421px;
    font-family: "Open Sans", sans-serif; font-size: 27px; letter-spacing: 2px; color: var(--on-night);
  }
</style>
</head>
<body>
  <section class="card card--front">
    <div class="brand-mark"></div>
    <div class="brand-name">
      <span class="brand-name__main">Dunstan &amp; Co</span>
      <span class="brand-name__sub">Lawyers &amp; Migration Agents</span>
    </div>

    <div class="person">
      <div class="person__name">Graham Dunstan</div>
      <div class="person__degree">BEc, LLB</div>
      <address class="person__address">Level 18, 72 Hollis Street<br>Australia, Sydney, NSW, 2000</address>
    </div>
    <div class="divider"></div>

    <ul class="contacts">
      <li>
        <svg viewBox="0 0 20 20"><circle cx="10" cy="10" r="9" fill="var(--accent)"/><path d="M6.5 5.5l2 2-1 1.3c.7 1.5 1.8 2.6 3.2 3.2l1.3-1 2 2-1.3 1.5c-3.6-.4-7-3.8-7.4-7.4z" fill="#fff"/></svg>
        +61 2 9384 5207
      </li>
      <li>
        <svg viewBox="0 0 20 20"><circle cx="10" cy="10" r="9" fill="var(--accent)"/><rect x="7" y="4.5" width="6" height="11" rx="1" fill="#fff"/><rect x="8" y="6" width="4" height="6" fill="var(--accent)"/></svg>
        0428316540
      </li>
      <li>
        <svg viewBox="0 0 20 20"><circle cx="10" cy="10" r="9" fill="var(--accent)"/><rect x="5" y="6.5" width="10" height="7" fill="#fff"/><path d="M5 6.5l5 4 5-4" fill="none" stroke="var(--accent)" stroke-width="1"/></svg>
        graham@permitpath-example.org.au
      </li>
      <li>
        <svg viewBox="0 0 20 20"><circle cx="10" cy="10" r="9" fill="var(--accent)"/><circle cx="10" cy="10" r="5" fill="none" stroke="#fff" stroke-width="1.3"/><path d="M5 10h10M10 5v10" stroke="#fff" stroke-width="1.1"/></svg>
        www.permitpath-example.org.au
      </li>
    </ul>

    <svg class="wave" width="885" height="506" viewBox="0 0 885 506" aria-hidden="true">
      <path d="M0 412 C190 448 350 482 545 458 C700 438 800 442 885 482 L885 506 L0 506 Z" fill="var(--accent)"/>
      <path d="M0 430 C190 468 350 498 545 472 C700 452 800 458 885 494 L885 506 L0 506 Z" fill="var(--paper)"/>
      <path d="M0 440 C190 478 350 506 545 480 C700 460 800 466 885 500 L885 506 L0 506 Z" fill="var(--night)"/>
      <path d="M0 448 C160 470 330 480 520 462 C690 446 790 448 885 470 L885 506 L0 506 Z" fill="var(--night)"/>
    </svg>
  </section>

  <section class="card card--back">
    <div class="back-mark"><span class="back-mark__name">Dunstan &amp; Co</span></div>
    <div class="back-url">www.permitpath-example.org.au</div>
  </section>
</body>
</html>
```